Web Design Project

Update to the following web page.

www.velontrigadvisory.com

We would like a full screen website, similar to the ones found here. http://www.pixelhonors.net/websites/fullscreen/

We also really like this site
http://bramwickstudio.com/

We would like new images and graphics.

Menu should be
1. Audit Defense
2. Education
3. Consulting
4. Outsourcing
5. Our Team
6. Store
7. Contact Us

Incorporate our new logo and colors. File is attached. The blue logo.

We want to add this tag line: "A passion for compliance through homecare and hospice training, education, and consulting."

Target Market(s)

Home Health Care Companies

Industry/Entity Type

Defense

Requirements
Must have
• Display our contact information in header and footer.

```html
<!DOCTYPE html>
<html lang="en">
<head>
<meta charset="utf-8">
<title>Velontrig Advisory</title>
<link href="https://fonts.googleapis.com/css2?family=Roboto+Condensed:wght@300;400&display=swap" rel="stylesheet">
<style>
  :root {
    --ink-navy: #1e3556;
    --logo-slate: #5a6f8f;
    --accent-red: #e8412f;
    --accent-blue: #33567f;
    --panel-dark: rgba(21, 36, 56, 0.86);
    --social-blue: #4a6a92;
    --band-grey: #c9d0d6;
    --white: #ffffff;
  }
  * { margin: 0; padding: 0; box-sizing: border-box; }
  html, body { width: 1200px; height: 784px; overflow: hidden; }
  body {
    position: relative;
    font-family: "Roboto Condensed", "Arial Narrow", sans-serif;
    color: var(--ink-navy);
    background: #e9edf0;
  }
  .backdrop {
    position: absolute; inset: 0;
    background:
      linear-gradient(100deg, rgba(255,255,255,0.55) 0%, rgba(255,255,255,0) 30%),
      linear-gradient(180deg, #eef1f3 0%, #d9dfe4 14%, #7f8e9c 30%, #9aa7b2 60%, #dfe4e8 74%, #eceff1 100%);
  }
  .site-header {
    position: absolute; left: 0; top: 0; width: 1200px; height: 114px;
    background: rgba(255,255,255,0.6);
  }
  .main-nav {
    position: absolute; top: 47px;
    display: flex; font-size: 16px; font-weight: 400; white-space: nowrap;
  }
  .main-nav a { color: var(--ink-navy); text-decoration: none; text-transform: uppercase; }
  .main-nav--left { left: 113px; }
  .main-nav--left a:nth-child(1) { margin-right: 16px; }
  .main-nav--left a:nth-child(2) { margin-right: 20px; }
  .main-nav--left a:nth-child(3) { margin-right: 20px; }
  .main-nav--right { left: 751px; }
  .main-nav--right a { margin-right: 20px; }
  .brand {
    position: absolute; left: 494px; top: 38px;
    display: flex; align-items: center; gap: 12px; white-space: nowrap;
    font-size: 19px; font-weight: 400; color: var(--logo-slate);
  }
  .brand__mark { width: 30px; height: 30px; background: var(--logo-slate); }
  .hero {
    position: absolute; left: 104px; top: 114px; width: 1006px; height: 460px;
    background: var(--panel-dark);
  }
  .social {
    position: absolute; left: 38px; top: 83px;
    display: flex; flex-direction: column; gap: 2px;
  }
  .social span { display: block; width: 36px; height: 36px; background: var(--social-blue); }
  .tagline {
    position: absolute; left: 86px; top: 83px;
    font-weight: 400; font-size: 19.5px; color: var(--white);
    text-transform: uppercase; white-space: nowrap;
  }
  .tagline span { display: block; width: max-content; height: 31px; line-height: 31px; padding: 0 9px; }
  .tagline__line--red { background: var(--accent-red); }
  .tagline__line--blue { background: var(--accent-blue); margin-top: 4px; }
  .intro {
    position: absolute; left: 93px; top: 160px;
    font-size: 14.5px; font-weight: 300; line-height: 19.8px;
    color: var(--white); white-space: nowrap;
  }
  .cta {
    position: absolute; left: 86px; top: 320px; width: 94px; height: 30px;
    background: var(--accent-red); color: var(--white); text-decoration: none;
    font-size: 15px; font-weight: 300; line-height: 30px; text-align: center;
  }
  .divider { position: absolute; left: 0; top: 574px; width: 1200px; height: 6px; background: var(--band-grey); }
  .site-footer { position: absolute; left: 0; top: 580px; width: 1200px; height: 204px; background: rgba(255,255,255,0.55); }
  .contact {
    position: absolute; left: 142px; top: 33px;
    font-size: 15px; font-weight: 300; line-height: 22.5px; font-style: normal; white-space: nowrap;
  }
  .contact__phone { display: flex; align-items: center; gap: 6px; }
  .footer-nav {
    position: absolute; right: 98px; top: 36px;
    display: flex; gap: 15px; font-size: 12px; white-space: nowrap;
  }
  .footer-nav a { color: var(--ink-navy); text-decoration: none; text-transform: uppercase; }
</style>
</head>
<body>
  <div class="backdrop" role="img" aria-label="Photo of travellers walking along a bright glass airport walkway with a moving sidewalk"></div>

  <header class="site-header">
    <nav class="main-nav main-nav--left">
      <a href="#">Home</a><a href="#">Audit Defense</a><a href="#">Education</a><a href="#">Consulting</a>
    </nav>
    <div class="brand"><span class="brand__mark"></span>VELONTRIG ADVISORY</div>
    <nav class="main-nav main-nav--right">
      <a href="#">Outsourcing</a><a href="#">Our Team</a><a href="#">Store</a><a href="#">Contact Us</a>
    </nav>
  </header>

  <main class="hero">
    <div class="social" aria-label="Social links">
      <span></span><span></span><span></span>
    </div>
    <h1 class="tagline">
      <span class="tagline__line--red">A passion for compliance through homecare</span>
      <span class="tagline__line--blue">and hospice training, education &amp; consultingme</span>
    </h1>
    <p class="intro">With over 100 years of combined experience in home health care, we have<br>compiled a very strong team of consultants to meet any challenge home<br>health agencies may face today! We are committed t<br>o providing the highest quality consulting services to our clients!<br>From new startups and small agencies to the largest Agencies in the country,<br>we provide a full range of problem solving consulting services to the Home<br>Health Care Industry.</p>
    <a class="cta" href="#">LEARN MORE</a>
  </main>

  <div class="divider"></div>

  <footer class="site-footer">
    <address class="contact">
      Velontrig &amp; Associates, LLC ©2013<br>
      418 Harlow Crest Drive<br>
      Suite 210<br>
      Brenford, MI, 48390<br>
      <span class="contact__phone">
        <svg width="17" height="17" viewBox="0 0 17 17" aria-hidden="true">
          <rect width="17" height="17" rx="3" fill="#1e3556"/>
          <path d="M5 3.5c.6 0 1 .3 1.2.8l.7 1.8c.1.4 0 .8-.3 1l-.8.6c.6 1.2 1.5 2.1 2.7 2.7l.6-.8c.3-.3.7-.4 1-.3l1.8.7c.5.2.8.6.8 1.2v.9c0 .6-.5 1-1.1 1C7.6 13 4 9.4 4 4.6c0-.6.4-1.1 1-1.1z" fill="#ffffff"/>
        </svg>
        (555) 318-4072
      </span>
    </address>
    <nav class="footer-nav">
      <a href="#">Home</a><a href="#">Audit Defense</a><a href="#">Education</a><a href="#">Consulting</a><a href="#">Outsourcing</a><a href="#">Our Team</a><a href="#">Store</a><a href="#">Contact Us</a>
    </nav>
  </footer>
</body>
</html>
```